Design a premium label for the most expensive honey in the world: Manuka honey.

Manuka honey is originaire from New Zealand and recognized for its natural antibacterial activity. Rare and expensive, it is used in hospital as medical grade mainly to cure burns and wounds... Household will use it out of a pot like a "supplement" or to cure all sorts of ailments.
The label must feel:
- Premium and elegant .
- Reflect strongly its origin New Zealand. Use maori design but be careful of copyright. Must be styled.
- Purity and trust it is the real deal. Feel strongly that it is not an ersatz...
- Health and "medical" use.
Label must have:
* Brand: WAREMU DOWNS
* MANUKA HONEY
* Made in New Zealand
* e250g
* MGO300
Target Market(s)
Export.

```html
<!DOCTYPE html>
<html lang="en">
<head>
<meta charset="utf-8">
<title>Waremu Downs Pure Manuka Honey Label</title>
<link rel="stylesheet" href="https://fonts.googleapis.com/css2?family=Marcellus&display=swap">
<style>
  :root {
    --page: #ffffff;
    --label-cream: #fdf9a1;
    --label-olive: #d0c65c;
    --ink: #0d0b08;
    --edge: #1a1a1a;
  }
  html, body {
    margin: 0;
    padding: 0;
    width: 909px;
    height: 1200px;
    overflow: hidden;
    background: var(--page);
  }
  .label {
    display: block;
    width: 909px;
    height: 1200px;
  }
  .label__hexagon {
    stroke: var(--edge);
    stroke-width: 1.5;
  }
  .label__text {
    font-family: "Marcellus", "Times New Roman", serif;
    fill: var(--ink);
    text-anchor: middle;
  }
  .label__brand { font-size: 166px; }
  .label__product { font-size: 86px; }
  .label__origin { font-size: 47px; }
  .label__spec { font-size: 40px; }
</style>
</head>
<body>
<svg class="label" viewBox="0 0 909 1200" xmlns="http://www.w3.org/2000/svg">
  <defs>
    <radialGradient id="koru-tone" cx="0.5" cy="0.45" r="0.62">
      <stop offset="0" stop-color="var(--label-cream)"/>
      <stop offset="0.55" stop-color="#ebe17e"/>
      <stop offset="1" stop-color="var(--label-olive)"/>
    </radialGradient>
    <clipPath id="hex-clip">
      <polygon points="454.5,75 909,337.5 909,862.5 454.5,1125 0,862.5 0,337.5"/>
    </clipPath>
  </defs>

  <polygon class="label__hexagon" fill="var(--label-cream)"
           points="454.5,75 909,337.5 909,862.5 454.5,1125 0,862.5 0,337.5"/>

  <g class="label__ornament" clip-path="url(#hex-clip)" role="img"
     aria-label="Stylised Maori koru swirl pattern in olive gold behind the lettering">
    <rect x="0" y="75" width="909" height="1050" fill="url(#koru-tone)" opacity="0.75"/>
  </g>

  <polygon fill="none" class="label__hexagon"
           points="454.5,75 909,337.5 909,862.5 454.5,1125 0,862.5 0,337.5"/>

  <text class="label__text label__brand" x="454.5" y="435">WAREMU</text>
  <text class="label__text label__brand" x="454.5" y="587">DOWNS</text>
  <text class="label__text label__product" x="454.5" y="701">Pure Manuka Honey</text>
  <text class="label__text label__origin" x="454.5" y="947">Made in New Zealand</text>
  <text class="label__text label__spec" x="454.5" y="1013">e250g</text>
  <text class="label__text label__spec" x="454.5" y="1060">MGO300</text>
</svg>
</body>
</html>
```